business card and flyer/pricelist

Business Name: Willow Strand Salon
new boutique salon run from home, using Australian owned natural products and colours, we need a flyer design to do a letter box drop to advertise the business as well as incorporating a price list on the front (single sided with writing on front and only colour on back)

The salon has a natural feel with light coloured timber chairs, bamboo timber bench top and shelving.

we are after a natural toned colour for the flyer, with possibly a brown/darkish colour writing

we are after a flyer that will also be able to use the design heading (business name) for business cards as well

feel free to look on my pintrest account to get a feel for my style under Corinne Belvane.

I love simple clean and Natural looks.

Industry/Entity Type

Boutique

Font styles to use
Script
Other font styles liked:
• SCRIPT HANDWRITTEN FONTS

Colors
cadf82
e9f1ce
5c5c5c
d3d3d3
add136
fee18a

Requirements
Must have
• NATURAL COLOURINGS, eg soft greens, browns,
white or off white background.
Should not have
• photos,

```html
<!DOCTYPE html>
<html lang="en">
<head>
<meta charset="utf-8">
<title>Willow Strand Salon – Flyer and Price List</title>
<link rel="stylesheet" href="https://fonts.googleapis.com/css2?family=Source+Sans+3:wght@400;600&family=Caveat:wght@500&display=swap">
<style>
  :root {
    --leaf: #add136;
    --sage: #cadf82;
    --cream: #e9f1ce;
    --charcoal: #5c5c5c;
    --mist: #d3d3d3;
    --sun: #fee18a;
    --ink: #4a4a44;
    --stage: #ececec;
  }
  * { margin: 0; padding: 0; box-sizing: border-box; }
  html, body { width: 1200px; height: 900px; overflow: hidden; }
  body {
    background: radial-gradient(ellipse at 50% 40%, #fafafa 0%, var(--stage) 60%, var(--mist) 100%);
    font-family: "Source Sans 3", Arial, sans-serif;
    position: relative;
  }
  .flyer {
    position: absolute;
    top: 70px;
    width: 362px;
    height: 760px;
    overflow: hidden;
    box-shadow: 0 4px 14px rgba(0,0,0,0.18);
  }
  .flyer--back { left: 210px; background: var(--charcoal); }
  .flyer--front {
    left: 628px;
    background: linear-gradient(170deg, #e2eec0 0%, var(--cream) 55%, #eef4d8 100%);
  }
  .brand {
    color: var(--leaf);
    font-weight: 400;
    line-height: 1;
  }
  .brand__name { font-size: 34px; letter-spacing: 0.5px; }
  .flyer--back .brand {
    position: absolute;
    left: 40px;
    top: 500px;
  }
  .flyer--front .brand {
    position: absolute;
    left: 34px;
    top: 58px;
  }
  .price-list {
    position: absolute;
    left: 40px;
    top: 150px;
    width: 240px;
    border-collapse: collapse;
    font-size: 11px;
    color: var(--ink);
  }
  .price-list td { padding: 0; line-height: 13.4px; }
  .price-list .price { text-align: right; white-space: nowrap; }
  .price-list .section td { font-weight: 600; letter-spacing: 0.3px; }
  .landscape {
    position: absolute;
    left: 0;
    bottom: 0;
    width: 362px;
    height: 210px;
    display: block;
  }
  .contact {
    position: absolute;
    left: 46px;
    bottom: 46px;
    list-style: none;
    font-family: "Caveat", "Comic Sans MS", cursive;
    font-size: 27px;
    color: var(--cream);
  }
  .contact__item {
    display: flex;
    align-items: center;
    gap: 12px;
    height: 36px;
  }
  .contact__icon {
    width: 24px;
    height: 24px;
    border-radius: 50%;
    background: var(--leaf);
    display: flex;
    align-items: center;
    justify-content: center;
    flex: none;
  }
  .contact__icon svg { width: 14px; height: 14px; }
</style>
</head>
<body>

  <section class="flyer flyer--back" aria-label="Flyer back">
    <div class="brand"><span class="brand__name">Willow Strand Salon</span></div>
  </section>

  <section class="flyer flyer--front" aria-label="Flyer front with price list">
    <div class="brand"><span class="brand__name">Willow Strand Salon</span></div>

    <table class="price-list">
      <tr class="section"><td>CUTS</td><td class="price"></td></tr>
      <tr><td>Ladies (inc. shampoo/blowdry)</td><td class="price">$45</td></tr>
      <tr><td>Mens</td><td class="price">$20</td></tr>
      <tr><td>13 &amp; Under</td><td class="price">From $15</td></tr>
      <tr><td>5 &amp; Under</td><td class="price">$10</td></tr>
      <tr class="section"><td>BLOWDRY &amp; STYLING</td><td class="price"></td></tr>
      <tr><td>Short</td><td class="price">$25</td></tr>
      <tr><td>Medium</td><td class="price">$30</td></tr>
      <tr><td>Long</td><td class="price">$40</td></tr>
      <tr><td>Straight Iron (after blowdry)</td><td class="price">$10</td></tr>
      <tr><td>Upstyles</td><td class="price">From $60</td></tr>
      <tr><td>Onsite styling</td><td class="price">POA</td></tr>
      <tr class="section"><td>COLOURS</td><td class="price"></td></tr>
      <tr><td>Regrowth</td><td class="price">$55</td></tr>
      <tr><td>Short</td><td class="price">$60</td></tr>
      <tr><td>Medium</td><td class="price">$75</td></tr>
      <tr><td>Long</td><td class="price">$85</td></tr>
      <tr class="section"><td>FOILS</td><td class="price"></td></tr>
      <tr><td>Top Foils</td><td class="price">$50</td></tr>
      <tr><td>½ head</td><td class="price">$95</td></tr>
      <tr><td>¾ head</td><td class="price">$110</td></tr>
      <tr><td>Full head</td><td class="price">$145</td></tr>
      <tr><td>(all include toner)</td><td class="price"></td></tr>
      <tr class="section"><td>TREATMENTS</td><td class="price"></td></tr>
      <tr><td>At basin</td><td class="price">$10</td></tr>
      <tr><td>Special Feel</td><td class="price">$35</td></tr>
      <tr><td>Eye brow/lash treatments</td><td class="price">From $10</td></tr>
    </table>

    <svg class="landscape" viewBox="0 0 362 210" aria-hidden="true">
      <path d="M0 34 Q70 2 170 8 Q250 16 300 36 L362 54 L362 210 L0 210 Z" fill="var(--sun)"/>
      <path d="M70 38 Q200 4 362 30 L362 210 L0 210 Z" fill="var(--sage)"/>
      <path d="M0 62 Q180 22 362 50 L362 210 L0 210 Z" fill="var(--charcoal)"/>
    </svg>

    <ul class="contact">
      <li class="contact__item">
        <span class="contact__icon">
          <svg viewBox="0 0 14 14"><path d="M7 2 L1.5 7 H3 V12 H6 V9 H8 V12 H11 V7 H12.5 Z" fill="var(--charcoal)"/></svg>
        </span>
        Your address
      </li>
      <li class="contact__item">
        <span class="contact__icon">
          <svg viewBox="0 0 14 14"><path d="M3.2 1.5 L5 1.3 L6.2 4.2 L5 5.2 Q6 7.6 8.8 9 L9.8 7.8 L12.7 9 L12.5 10.8 Q11.8 12.6 10 12.4 Q3.4 11.2 1.6 4 Q1.4 2.2 3.2 1.5 Z" fill="var(--charcoal)"/></svg>
        </span>
        000 123 45666
      </li>
      <li class="contact__item">
        <span class="contact__icon"></span>
        Corinne Belvane
      </li>
    </ul>
  </section>

</body>
</html>
```